依頼詳細
建設業界では、まだ段階の世代で古き良き
日本というカテゴリが強く残っている現状ですが
大手スーパーゼネコンのように、現代の最先端のユーモアさも取り入れ
他の建設業界とは、一風変わった特徴ある名刺を作成したいと
考えて応募しました。
記載項目
株式会社 DAVRO
代表取締役 高野 典久
希望イメージ
シンプル 複雑
単色 カラフル
暗い 明るい
日常 高級
遊び心 厳粛
未来的 伝統的
女性的 男性的
希望する色
オレンジ
納品ファイル
• 高解像度JPG (.jpg)
• フォトショップ形式 (.psd)
補足説明
当社のロゴのdataを追加しました。

ですが必ずしもロゴを記載したいというわけではございません
自分自身は趣味でヨーロッパなどの歴史ある建造物などを
見に足を運ぶなどもしております。(^^)
■ 選んだ理由

横のデザイン構成・全体的なバランス
がとても気に入り決断致しました。

■ 提案者全員のお礼・コメント

この度は皆様方に
様々なご提案、ご参加いただき
誠にお礼を申し上げる次第です。

ありがとうございます。

```html
<!DOCTYPE html>
<html lang="ja">
<head>
<meta charset="utf-8">
<title>株式会社 DAVRO 名刺</title>
<link rel="stylesheet" href="https://fonts.googleapis.com/css2?family=Noto+Sans+JP:wght@400;500;700;900&display=swap">
<style>
  :root {
    --orange: #f39a1e;
    --orange-light: #f7b84a;
    --ink: #1a1a1a;
    --ink-soft: #333333;
    --paper: #ffffff;
    --brick-top: #e8a67a;
    --brick-mid: #d98a5c;
    --brick-low: #c97347;
  }
  * { margin: 0; padding: 0; box-sizing: border-box; }
  html, body { width: 722px; height: 1200px; overflow: hidden; background: var(--paper); }
  body { font-family: "Noto Sans JP", sans-serif; color: var(--ink); }

  .card { position: relative; width: 722px; height: 1200px; background: var(--paper); overflow: hidden; }

  .top-band {
    position: absolute; left: 0; top: 0; width: 100%; height: 46px;
    background: linear-gradient(180deg, var(--orange-light), var(--orange));
  }

  .brand {
    position: absolute; top: 152px; left: 0; width: 100%; height: 80px;
    display: flex; justify-content: center; align-items: center; gap: 16px;
  }
  .brand-mark { width: 80px; height: 80px; border-radius: 50%; background: var(--orange); flex: none; }
  .brand-name { font-weight: 900; font-size: 40px; line-height: 1; color: var(--orange); letter-spacing: 0.02em; }

  .person { position: absolute; left: 252px; top: 376px; }
  .person-title { font-size: 24px; line-height: 30px; font-weight: 500; color: var(--ink-soft); }
  .person-name { margin-top: 22px; font-size: 36px; line-height: 44px; font-weight: 700; letter-spacing: 0.06em; }
  .person-roman { margin-top: 4px; font-size: 22px; line-height: 28px; color: var(--ink-soft); }

  .company { position: absolute; left: 89px; top: 592px; }
  .company-name { font-size: 24px; line-height: 40px; font-weight: 500; white-space: nowrap; }
  .company-name .latin { font-size: 32px; font-weight: 700; }

  .contact-list { list-style: none; margin-top: 4px; }
  .contact-list li {
    display: flex; align-items: center; gap: 6px;
    height: 38.5px; font-size: 24px; line-height: 1; color: var(--ink); white-space: nowrap;
  }
  .contact-icon {
    display: inline-flex; align-items: center; justify-content: center; flex: none;
    width: 32px; height: 20px; border-radius: 3px;
    background: var(--orange); color: var(--paper);
    font-size: 11px; font-weight: 700; line-height: 1;
  }
  .contact-icon svg { width: 20px; height: 14px; }

  .brick-wall {
    position: absolute; left: 0; top: 848px; width: 100%; height: 352px;
    background: linear-gradient(180deg, var(--brick-mid) 0%, var(--brick-low) 45%, var(--brick-top) 100%);
  }
</style>
</head>
<body>
<main class="card">
  <div class="top-band"></div>

  <header class="brand">
    <span class="brand-mark"></span>
    <span class="brand-name">株式会社 DAVRO</span>
  </header>

  <section class="person">
    <p class="person-title">代表取締役</p>
    <p class="person-name">高野　典久</p>
    <p class="person-roman">Norihisa Takano</p>
  </section>

  <section class="company">
    <p class="company-name">株式会社<span class="latin">DAVRO</span></p>
    <ul class="contact-list">
      <li><span class="contact-icon">〒</span>000-0000 〇〇〇〇〇〇〇〇〇〇〇1-1-1</li>
      <li><span class="contact-icon">TEL</span>03-0000-0000</li>
      <li><span class="contact-icon">FAX</span>03-0000-0000</li>
      <li><span class="contact-icon">Mob</span>000-0000-0000</li>
      <li><span class="contact-icon"><svg viewBox="0 0 20 14" fill="none" stroke="#fff" stroke-width="1.6"><rect x="1" y="1" width="18" height="12"/><path d="M1 1l9 7 9-7"/></svg></span>aaabbb@ccc.co.jp</li>
    </ul>
  </section>

  <div class="brick-wall" role="img" aria-label="Terracotta brick wall pattern across the bottom of the card"></div>
</main>
</body>
</html>
```